Cyber Security firm working in the Financial Services sector needs a brochure

We need a brochure covering our products and offerings. We work exclusively with Independent Broker Dealers, their Reps and RIAs in the US. We help them keep their computers secure and compliant with applicable regulations and policies. Have attached samples of our logo an descriptions of our products and services.

Financial Institutions and Financial Advisors

Financial Service

```html
<!DOCTYPE html>
<html lang="en">
<head>
<meta charset="utf-8">
<title>Services Brochure</title>
<link href="https://fonts.googleapis.com/css2?family=Source+Sans+3:ital,wght@0,400;0,600;0,700;1,600&display=swap" rel="stylesheet">
<style>
:root{
  --brand:#1b4a9e;
  --brand-deep:#143c85;
  --ink:#2b2b2b;
  --paper:#ffffff;
  --backdrop:#e9e9e9;
}
*{box-sizing:border-box;margin:0;padding:0}
html,body{width:1200px;height:1200px;overflow:hidden;background:var(--backdrop)}
body{font-family:"Source Sans 3",Arial,sans-serif;color:var(--ink)}
.page{position:absolute;left:136px;top:0;width:927px;height:1200px;background:var(--paper);overflow:hidden}
.service{position:absolute;width:404px}
.service.left{left:52px}
.service.right{left:482px}
.service-head{display:flex;align-items:center;gap:16px;margin-bottom:6px}
.service-icon{width:63px;height:63px;flex:none}
.service-title{font-style:italic;font-weight:600;font-size:25px;line-height:31px;color:var(--brand)}
.service p{font-size:14px;line-height:18.3px;text-align:justify;hyphens:auto}
.price{color:var(--brand);font-weight:600}
.config-panel{position:absolute;left:0;top:318px;width:454px;height:483px;background:var(--brand);color:#fff;padding:14px 12px 0 54px}
.config-panel::before{content:"";position:absolute;left:95px;top:-1px;border-left:9px solid transparent;border-right:9px solid transparent;border-top:10px solid var(--paper)}
.config-panel h3{font-style:italic;font-weight:600;font-size:17px;line-height:22px;margin:0 0 4px}
.config-panel ul{list-style:none;margin-bottom:8px}
.config-panel li{position:relative;padding-left:22px;font-size:14px;line-height:18.2px}
.config-panel li::before{content:"";position:absolute;left:7px;top:6px;width:7px;height:7px;border-radius:50%;background:#fff}
.config-panel h3.safety{margin-top:14px;margin-bottom:8px}
.footer-band{position:absolute;left:0;bottom:0;width:927px;height:83px}
</style>
</head>
<body>
<main class="page">

  <section class="service left" style="top:35px">
    <div class="service-head">
      <svg class="service-icon" viewBox="0 0 64 64"><circle cx="32" cy="32" r="32" fill="var(--brand)"/><rect x="18" y="20" width="26" height="18" rx="1.5" fill="none" stroke="#fff" stroke-width="2.5"/><path d="M14 41h34l-3 4H17z" fill="#fff"/><path d="M23 33l9-9M27 34l10-10" stroke="#fff" stroke-width="2"/><path d="M44 15a6 6 0 0 1 5 5M44 11a10 10 0 0 1 9 9" fill="none" stroke="#fff" stroke-width="2"/></svg>
      <h2 class="service-title">New Computer<br>Sourcing</h2>
    </div>
    <p>We are an authorized Norvane Value Added Reseller and will be happy to help you get your new computer. We work with you to determine an appropriate configuration and what would be a good fit for your specific needs.</p>
  </section>

  <section class="service left" style="top:190px">
    <div class="service-head">
      <svg class="service-icon" viewBox="0 0 64 64"><circle cx="32" cy="32" r="32" fill="var(--brand)"/><rect x="15" y="24" width="24" height="17" rx="1.5" fill="none" stroke="#fff" stroke-width="2.5"/><path d="M11 44h32l-3 4H14z" fill="#fff"/><path d="M40 13l10 4v8c0 7-5 11-10 13-5-2-10-6-10-13v-8z" fill="#fff"/><path d="M40 17v18" stroke="var(--brand)" stroke-width="2"/></svg>
      <h2 class="service-title">New Computer<br>Configuration</h2>
    </div>
    <p>Configuration services provided for new computers. These can be sourced from us or locally and shipped to us or done remotely. <span class="price">Price $300.</span></p>
  </section>

  <section class="config-panel">
    <h3>Configure for Broker Dealer security requirements</h3>
    <ul>
      <li>Encrypt the Drive</li>
      <li>Set password Policy</li>
      <li>Set Screen saver timeout policy</li>
      <li>Apply all Operating System patches</li>
      <li>Set computer for Auto-update of all products where possible (if not subscribing to our Managed Software Patching service)</li>
      <li>Install default Anti-Virus software and configure to policy requirements (if not subscribing to our Managed Anti-Virus service)</li>
    </ul>
    <h3>Configure for functionality</h3>
    <ul>
      <li>Remove any unneeded software</li>
      <li>Configure browsers to function most reliably with BD sites</li>
      <li>Remove any unneeded Browser Plug-ins or Tool Bars</li>
      <li>Install Javelin runtime (as required)</li>
      <li>Install Pagefold Reader</li>
      <li>Install Quillworks Office if needed –<br>We can provide Office for $199</li>
    </ul>
    <h3 class="safety">Safety</h3>
    <ul>
      <li>Create a System Image to an external encrypted drive</li>
      <li>Create Encryption Recovery media and keys if applicable</li>
    </ul>
  </section>

  <section class="service left" style="top:817px">
    <div class="service-head">
      <svg class="service-icon" viewBox="0 0 64 64"><circle cx="32" cy="32" r="32" fill="var(--brand)"/><path d="M18 36v-6a14 14 0 0 1 28 0v6" fill="none" stroke="#fff" stroke-width="3"/><rect x="15" y="33" width="8" height="13" rx="3" fill="#fff"/><rect x="41" y="33" width="8" height="13" rx="3" fill="#fff"/><path d="M45 46c0 5-5 7-10 7" fill="none" stroke="#fff" stroke-width="2.5"/><circle cx="33" cy="53" r="2.5" fill="#fff"/></svg>
      <h2 class="service-title">General Computer<br>Support</h2>
    </div>
    <p>SecureLedger has a long history of working with thousands of Independent Financial Advisors and Broker Dealers across the country. Because of this we have a lot of experience in supporting their technology needs. A benefit of this is we not only understand the technology but also the special needs of the financial services industry. All our technicians are US based, have years of industry experience and must pass a rigorous background check. We also understand your security requirements and will execute appropriate non-disclosure agreements to help you insure your information remains private. We've found we can resolve most software and configuration issues remotely. <span class="price">Our rates are $95 per hour.</span></p>
  </section>

  <section class="service right" style="top:33px">
    <div class="service-head">
      <svg class="service-icon" viewBox="0 0 64 64"><circle cx="32" cy="32" r="32" fill="var(--brand)"/><rect x="14" y="20" width="34" height="24" rx="2" fill="none" stroke="#fff" stroke-width="2.5"/><rect x="19" y="25" width="20" height="14" fill="#fff"/><path d="M36 40l13-17 3 2-13 17-4 1z" fill="#fff" stroke="var(--brand)" stroke-width="1.2"/></svg>
      <h2 class="service-title">Security Awareness<br>Training</h2>
    </div>
    <p>Security Awareness Training is a critical component of a comprehensive cyber security program. Because the cyber security environment is continuously changing, it is our experience that a multi-level approach is most effective in providing timely, actionable information as well as a firm grasp of critical security principals and requirements.<br>Our first level is a targeted, electronic delivery of mini-training modules, typically taking no longer than 10 minutes to complete, every 4-6 weeks. These short, topical modules are designed to highlight current attacks and the appropriate response to the illustrated threat. The attacks are explained in an easy-to-understand format with the amount of technical jargon kept to the bare minimum. Each module presents several multiple choice questions to insure the respondent has a firm grasp of the topic. The continuous, “drip” nature of this timely information is important in keeping security top-of-mind.<br>Our second level provides periodic phishing emails. The emails consist of both general phishing emails, spear phishing, as well as very targeted “whaling” types of email. Anyone found susceptible to opening specially crafted attachments or links will be immediately taken to an on-line refresher course on how to spot fraudulent emails. <span class="price">$25 per user per year.</span></p>
  </section>

  <section class="service right" style="top:502px">
    <div class="service-head">
      <svg class="service-icon" viewBox="0 0 64 64"><circle cx="32" cy="32" r="32" fill="var(--brand)"/><path d="M12 26a28 28 0 0 1 40 0M18 32a20 20 0 0 1 28 0M24 38a12 12 0 0 1 16 0" fill="none" stroke="#fff" stroke-width="4" stroke-linecap="round"/><circle cx="32" cy="45" r="4.5" fill="#fff"/></svg>
      <h2 class="service-title">Internet Blocking<br>and Filtering</h2>
    </div>
    <p>Comprehensive security for your network through award-winning phishing, botnet and malware site protection. Our web filtering service delivers network security services through the DNS layer blocking known malicious or infected sites from resolving on your network. This also allows you to block specific web sites and also broad categories of content from being accessed from your locations. A couple of examples might be Gambling and Pornography. <span class="price">$3.50 per month per device.</span></p>
  </section>

  <section class="service right" style="top:720px">
    <div class="service-head">
      <svg class="service-icon" viewBox="0 0 64 64"><circle cx="32" cy="32" r="32" fill="var(--brand)"/><g fill="#fff"><rect x="11" y="22" width="12" height="6"/><rect x="25" y="22" width="12" height="6"/><rect x="11" y="30" width="6" height="6"/><rect x="19" y="30" width="12" height="6"/><rect x="11" y="38" width="12" height="6"/><rect x="25" y="38" width="10" height="6"/></g><path d="M46 20c6 7 8 11 8 16a8 8 0 0 1-16 0c0-4 3-6 4-10 1 3 2 4 3 4 1-3 1-6 1-10z" fill="#fff"/></svg>
      <h2 class="service-title">Firewall<br>Sales</h2>
    </div>
    <p>We provide pre-purchase consulting, configuration and support for business grade firewalls. We will help you spec an appropriate firewall, determine if VPN access is needed as well as any dedicated guest Wireless Access. The most suitable device for your location as well as any satellite locations is dependent on organization size and complexity. <span class="price">Prices starting at $750.</span></p>
  </section>

  <section class="service right" style="top:906px">
    <div class="service-head">
      <svg class="service-icon" viewBox="0 0 64 64"><circle cx="32" cy="32" r="32" fill="var(--brand)"/><path d="M24 22a14 14 0 1 0 16 0" fill="none" stroke="#fff" stroke-width="4" stroke-linecap="round"/><path d="M32 16v16" stroke="#fff" stroke-width="4" stroke-linecap="round"/></svg>
      <h2 class="service-title">Public<br>IP Monitoring</h2>
    </div>
    <p>Knowing what the world sees of your front door to the internet is important. Our Public IP Monitoring scans your static IP address daily looking for inappropriate ports being made available over the internet. If we find your device has changes made we contact you to verify the changes were intentional and explain the ramifications of the changes. We don't want your network exposed because the Tech installing your new copier decided to open up a number of ports on your firewall.<br><span class="price">$100 per year per IP address.</span></p>
  </section>

  <svg class="footer-band" viewBox="0 0 927 83" preserveAspectRatio="none"><polygon points="0,0 927,46 927,83 0,83" fill="var(--brand)"/></svg>
</main>
</body>
</html>
```